Community Bank Web Design

Design a homepage and internal product page for a community bank. Needs to be mobile friendly, minimal scrolling on home. Create the homepage look & feel, then use the same aesthetic to create the product page for the personal checking account page.

Wireframes, logo variations, and color scheme attached.

New brand identity:
• Open, Fresh, Younger, Bright, Bold, New, Innovative.
• Inviting, approachable, friendly, trustworthy.
• Imagine a young family purchasing their first home as the target audience.
You do not have to stick to the exact layout of the wireframes, as long as all of the elements are present.

All navigation elements are specified in wireframes. There are three versions of the homepage – Personal Home, Business Home, Wealth Management Home – you may design whichever version you prefer.

For internal page – please design the Checking product page, included in wireframes.

NOTE: Submit your homepage design first. I will provide feedback on your design direction, then you can use that to move forward with the internal page design.

Design direction--
Some banking / financial sites we like for their fresh/bold/open look:
velmorant.com
quastel.ca
rpwfinancial.org
kdh.co.nz
yarbel.com
pettigrubank.com
uvm.co.nz

Target Market(s)

The target market for the personal homepage varies. Adults in the midwest, 25 - 60, who are striving to build their savings and manage their money. Often buying homes or refinancing their homes to make renovations, or planning for retirement.

For the business homepage, the target market are small to mid-market business owners striving to grow their business and manage their company.

Industry/Entity Type

Financial

Requirements
Must have
• colors: CRIMSON #a20c33,
FOREST GREEN #004f38
GOLD #e6a513

File format for design submission must be layered PSD (Please organize layers into recognizable folders like "menu" and "footer")

To make the design "mobile friendly" please create a grid-based layout. http://www.dorvané.com/patterns/showPattern.php?patternID=grid-based-layout
http://www.brindlequarterly.com/2007/04/14/designing-with-grid-based-approach/

```html
<!DOCTYPE html>
<html lang="en">
<head>
<meta charset="utf-8">
<title>Harrow Creek Bank – Personal Checking Accounts</title>
<link href="https://fonts.googleapis.com/css2?family=Open+Sans:wght@400;600;700&display=swap" rel="stylesheet">
<style>
:root{
  --crimson:#a20c33;
  --crimson-bright:#e3124a;
  --crimson-mid:#d01043;
  --forest:#004f38;
  --forest-light:#0a7a55;
  --gold:#e6a513;
  --gold-light:#f4b41c;
  --ink:#333;
  --muted:#9a9a9a;
  --line:#e2e2e2;
  --row:#ececec;
  --footer:#2e3031;
}
*{box-sizing:border-box;margin:0;padding:0}
html,body{width:835px;height:1200px;overflow:hidden;background:#fff}
body{position:relative;font-family:"Open Sans",Arial,sans-serif;color:var(--ink)}
.abs{position:absolute}

.accent-rule{left:0;top:0;width:835px;height:2px;background:linear-gradient(90deg,var(--crimson) 0 33%,var(--forest) 33% 67%,var(--gold) 67%)}
.utility{left:92px;top:2px;width:651px;height:26px;border-bottom:1px solid var(--line);font-size:7.5px;color:#444;display:flex;align-items:center}
.utility span{display:flex;align-items:center;gap:4px;margin-right:16px}
.utility .right{margin-left:auto;display:flex}
.utility .right span{margin:0 0 0 16px}
.utility svg{width:7px;height:7px;fill:var(--crimson)}

.brand{left:92px;top:58px;display:flex;align-items:center;gap:6px;font-size:15px;color:var(--crimson)}
.brand i{width:26px;height:26px;border-radius:50%;background:var(--crimson);display:block}
.search{left:649px;top:62px;width:94px;height:17px;border:1px solid var(--line);font-size:6.5px;color:#aaa;padding:4px 6px}

.main-nav{left:92px;top:113px;width:651px;height:28px;background:linear-gradient(#e3124a,var(--crimson-mid));display:flex;font-size:7.5px;color:#fff}
.main-nav a{padding:0 14px;line-height:28px;border-right:1px solid rgba(0,0,0,.15)}
.main-nav .login{margin-left:auto;border-right:0;border-left:1px solid rgba(0,0,0,.15);display:flex;align-items:center;gap:6px;padding:0 16px}

.sidebar{left:92px;top:162px;width:150px;height:908px;background:linear-gradient(#e3124a,var(--crimson) 100%)}
.sidebar h3{font-size:10px;color:#fff;font-weight:600;padding:13px 0 0 26px;height:35px;border-bottom:1px solid rgba(0,0,0,.08);display:flex;gap:6px}
.side-group{list-style:none;padding:9px 0 9px 30px;border-bottom:1px solid rgba(0,0,0,.08);font-size:7.5px;color:#fff;line-height:14px}
.side-group li::before{content:"•";margin:0 5px 0 -8px}

.crumbs{left:258px;top:163px;font-size:6.5px;color:#333;display:flex;gap:8px;align-items:center;border-bottom:1px solid var(--line);padding-bottom:4px}
.crumbs b{width:6px;height:6px;border:1px solid var(--crimson);border-radius:50%;display:block}
.page-title{left:258px;top:190px;font-size:16px;font-weight:400;color:#333}
.hero{left:258px;top:222px;width:485px;height:164px;background:linear-gradient(100deg,#6b5a3a,#c9a88a 35%,#8c9a55 60%,#b8c47a 90%)}

.copy{left:258px;top:400px;width:317px;font-size:7.3px;line-height:13.3px;color:var(--muted)}
.copy p{margin-bottom:13.3px}

.related{left:593px;top:403px;width:150px;height:173px;background:linear-gradient(#e3124a,var(--crimson))}
.related h4{text-align:center;font-size:9.5px;color:#fff;font-weight:600;padding-top:10px;height:29px}
.related ul{list-style:none}
.related li{height:29px;display:flex;align-items:center;gap:14px;padding-left:9px;font-size:7.5px;color:#fff;border-top:1px solid rgba(0,0,0,.08)}
.related svg{width:11px;height:11px}
.open-btn{left:593px;top:576px;width:150px;height:22px;background:var(--gold-light);color:#fff;font-size:7.5px;text-align:center;line-height:22px}

.section-title{left:258px;top:640px;font-size:13.5px;color:#333;font-weight:400}
.compare{left:258px;top:672px;width:485px;border-collapse:collapse;font-size:7.3px;color:var(--muted)}
.compare th{height:22px;background:linear-gradient(var(--forest-light),var(--forest));color:#fff;font-weight:400;border-left:1px solid rgba(255,255,255,.15)}
.compare td{height:22.3px;text-align:center;border:1px solid var(--line);border-width:0 1px}
.compare td:first-child{text-align:left;padding-left:16px;width:192px}
.compare td:nth-child(2){width:140px}
.compare tr:nth-child(odd) td{background:var(--row)}
.compare tr:last-child td{border-bottom:1px solid var(--line)}
.box{display:inline-block;width:10px;height:10px;border:1px solid #bbb;border-radius:2px;background:#fff;vertical-align:middle;position:relative}
.box.on::after{content:"";position:absolute;left:3px;top:0;width:3px;height:6px;border:solid #222;border-width:0 1.5px 1.5px 0;transform:rotate(40deg)}

.tabs{left:258px;top:872px;display:flex}
.tabs span{width:89.4px;height:25px;line-height:25px;text-align:center;font-size:7.5px;color:#fff;background:var(--crimson);border-right:1px solid rgba(0,0,0,.15)}
.tabs span.active{background:var(--crimson-bright)}
.panel{left:258px;top:897px;width:485px;height:173px;background:linear-gradient(#e3124a,var(--crimson));padding:18px 16px;color:#fff}
.panel h4{font-size:12px;font-weight:600;margin-bottom:11px}
.panel p{font-size:7.3px;line-height:13.3px}
.opt-btn{display:inline-block;margin-top:15px;background:var(--gold-light);font-size:7.5px;padding:4px 7px}

.footer{left:0;top:1115px;width:835px;height:85px;background:var(--footer)}
.footer-brand{left:92px;top:1137px;display:flex;align-items:center;gap:6px;font-size:15px;line-height:15px;color:#fff}
.footer-brand i{width:28px;height:28px;border-radius:50%;background:#fff;display:block}
.footer-links{left:298px;top:1145px;display:flex;gap:22px;font-size:8.8px;color:#fff}
.copyright{left:92px;top:1185px;font-size:6.2px;color:#777}
.social{left:680px;top:1177px;display:flex;gap:8px}
.social i{width:15px;height:15px;border:1px solid #666;border-radius:50%;display:block}
</style>
</head>
<body>
<div class="abs accent-rule"></div>

<div class="abs utility">
  <span><svg viewBox="0 0 10 10"><circle cx="5" cy="3" r="2.5"/><path d="M0 10c0-3 2-4.5 5-4.5s5 1.5 5 4.5z"/></svg>Personal</span>
  <span><svg viewBox="0 0 10 10"><rect x="0" y="3" width="10" height="7"/><rect x="3" y="1" width="4" height="2.5" fill="none" stroke="#a20c33"/></svg>Business</span>
  <span><svg viewBox="0 0 10 10"><rect y="1" width="10" height="2"/><rect y="4" width="10" height="2"/><rect y="7" width="10" height="2"/></svg>Wealth Management</span>
  <div class="right">
    <span><b style="color:var(--crimson)">$</b>Find a Branch or ATM</span>
    <span><svg viewBox="0 0 10 10"><ellipse cx="5" cy="4.5" rx="5" ry="4"/></svg>Contact Us</span>
  </div>
</div>

<div class="abs brand"><i></i>Harrow Creek Bank</div>
<div class="abs search">Search...</div>

<nav class="abs main-nav">
  <a>Products &amp; Services</a><a>Why HCB?</a><a>Customer Center</a>
  <a class="login"><svg width="7" height="8" viewBox="0 0 7 8"><rect y="3.5" width="7" height="4.5" fill="#fff"/><path d="M1.5 3.5V2.5a2 2 0 0 1 4 0v1" stroke="#fff" fill="none"/></svg>LOG IN</a>
</nav>

<aside class="abs sidebar">
  <h3><svg width="9" height="9" viewBox="0 0 10 10" fill="#fff"><circle cx="5" cy="3" r="2.5"/><path d="M0 10c0-3 2-4.5 5-4.5s5 1.5 5 4.5z"/></svg>Personal</h3>
  <ul class="side-group"><li>Checking Accounts</li><li>Debit Cards</li><li>Saving &amp; CDs</li></ul>
  <ul class="side-group"><li>Loans</li><li>Credit Cards</li></ul>
  <ul class="side-group"><li>Investing</li></ul>
  <ul class="side-group"><li>Online Banking</li><li>Mobile Banking</li></ul>
  <ul class="side-group"><li>Additional Services</li></ul>
</aside>

<div class="abs crumbs">Home <b></b> Products &amp; Services <b></b> Checking Accounts</div>
<h1 class="abs page-title">Personal Checking Accounts</h1>
<div class="abs hero" role="img" aria-label="Photo of a young couple sharing a laptop on a park bench"></div>

<div class="abs copy">
  <p>Lorem ipsum dolor sit amet, consectetur adipiscing elit. Nulla quam velit, vulputate eu pharetra nec, mattis ac neque. Duis vulputate commodo lectus, ac blandit elit tincidunt id. Sed rhoncus, tortor sed eleifend tristique, tortor mauris molestie elit, et lacinia ipsum quam nec dui.</p>
  <p>Quisque nec mauris sit amet elit iaculis pretium sit amet quis magna. Aenean velit odio, elementum in tempus ut, vehicula eu diam. Pellentesque rhoncus aliquam mattis.</p>
  <p>Ut vulputate eros sed felis sodales nec vulputate justo hendrerit. Vivamus varius pretium ligula, a aliquam odio euismod sit amet. Quisque laoreet sem sit amet orci ullamcorper at ultricies metus viverra.</p>
  <p>Pellentesque arcu mauris, malesuada quis ornare accumsan, blandit sed diam. Sed rhoncus, tortor sed eleifend tristique, tortor mauris molestie elit, et lacinia ipsum quam nec dui.</p>
</div>

<div class="abs related">
  <h4>Related Links</h4>
  <ul>
    <li><svg viewBox="0 0 12 12"><circle cx="6" cy="6" r="5.2" fill="none" stroke="#fff"/><path d="M5 3.8 7.2 6 5 8.2" fill="none" stroke="#fff"/></svg>Order Checks</li>
    <li><svg viewBox="0 0 12 12"><circle cx="6" cy="6" r="5.2" fill="none" stroke="#fff"/><path d="M5 3.8 7.2 6 5 8.2" fill="none" stroke="#fff"/></svg>Debit Card</li>
    <li><svg viewBox="0 0 12 12"><circle cx="6" cy="6" r="5.2" fill="none" stroke="#fff"/><path d="M5 3.8 7.2 6 5 8.2" fill="none" stroke="#fff"/></svg>Overdraft Protection</li>
    <li><svg viewBox="0 0 12 12"><circle cx="6" cy="6" r="5.2" fill="none" stroke="#fff"/><path d="M5 3.8 7.2 6 5 8.2" fill="none" stroke="#fff"/></svg>Mobile Banking</li>
    <li><svg viewBox="0 0 12 12"><circle cx="6" cy="6" r="5.2" fill="none" stroke="#fff"/><path d="M5 3.8 7.2 6 5 8.2" fill="none" stroke="#fff"/></svg>Switch Kit</li>
  </ul>
</div>
<div class="abs open-btn">OPEN CHECKING</div>

<h2 class="abs section-title">Compare Checking Accounts</h2>
<table class="abs compare">
  <tr><th></th><th>Free Checking</th><th>Interest Checking</th></tr>
  <tr><td>Free</td><td><span class="box on"></span></td><td><span class="box"></span></td></tr>
  <tr><td>Hundreds of ATMs</td><td><span class="box on"></span></td><td><span class="box on"></span></td></tr>
  <tr><td>.03% interest</td><td><span class="box"></span></td><td><span class="box on"></span></td></tr>
  <tr><td>Minimium to Open</td><td>$100</td><td>$300</td></tr>
  <tr><td>Minimum Balance Requirement</td><td>$0</td><td>$300</td></tr>
  <tr><td>Monthly Service Fee</td><td>$0</td><td>$5*</td></tr>
</table>

<div class="abs tabs">
  <span>Mobile Banking</span><span class="active">Overdraft Protection</span><span>Debit Card</span><span>Direct Deposit</span><span>Switch Kit</span>
</div>
<div class="abs panel">
  <h4>Overdraft Protection</h4>
  <p>Lorem ipsum dolor sit amet, consectetur adipiscing elit. Nulla quam velit, vulputate eu pharetra nec, mattis ac neque. Duis vulputate commodo lectus, ac blandit elit tincidunt id. Sed rhoncus, tortor sed eleifend tristique, tortor mauris molestie elit, et lacinia ipsum quam nec dui. Quisque nec mauris sit amet elit iaculis pretium sit amet quis magna. Aenean velit odio, elementum in tempus ut, vehicula eu diam. Pellentesque rhoncus aliquam mattis. Ut vulputate eros sed felis sodales nec vulputate justo hendrerit.</p>
  <span class="opt-btn">Opt In Today!</span>
</div>

<footer class="abs footer"></footer>
<div class="abs footer-brand"><i></i>Harrow Creek<br>Bank</div>
<div class="abs footer-links"><span>About</span><span>Careers</span><span>Privacy Policy</span><span>Member FDIC</span><span>Investor Relations Link</span><span>Security</span><span>CRA</span></div>
<div class="abs copyright">Copyright © 2014 Harrow Creek Bank. All Rights Reserved.</div>
<div class="abs social"><i></i><i></i><i></i></div>
</body>
</html>
```